Glenmorrow ice cream tub packaging

We need new tub designs for our dairy free ice cream. It is made with avocado and coconut which we would like communicated within the design. We launched last year and have had positive feedback regarding our current packaging but also that it could be a cleaner design with a more sophisticated font as it will be sold in more high end expensive stores. I have attached our current packaging for info (there are 3 flavours - Original Avocado, Raspberry and Basil, Raw Cacao) We would like to keep the avocado print that is currently included on the packaging as we have had a lot of very positive feedback about that. Maybe not as much though as it makes it quite busy and we prefer a clean design.
I've also attached our new logo.
We would like it to mention we are gluten, soya, dairy, egg and nut free. And that it is a 'coconut and avocado ice cream' rather than an 'alternative'.
The nutritional label needs to be in a UK table format (I've attached a blank copy for information). We don't currently have the values for the table as it has been sent off for testing as we have a new recipe. But if you could leave that blank we will fill it in when we have the results.
I've attached the template for the sizes as we have two sizes - 500ml and 100ml. The designs will be the same but just smaller/bigger. It has to be font size 11 for legal purpose.
It has to have the weight (100ml and 500ml) followed by the official e-mark.
The ingredients are the same but take out Locust Bean Gum and replace Vanilla extract with Lime Juice.
The business address is the same but should read 'Glenmorrow LTD'. All other info on the packaging (barcode, text etc) is to remain the same.
I've have also attached 3 pictures of other tub designs that we like for inspiration - our favourite is 'zelt' as we can have half the print half the colour if the flavour (raspberry/pink, cacao/brown, original/green)
Updates
Target Market(s)
High end health food stores
Look and feel

```html
<!DOCTYPE html>
<html lang="en">
<head>
<meta charset="utf-8">
<title>Glenmorrow ice cream tub packaging</title>
<link rel="stylesheet" href="https://fonts.googleapis.com/css2?family=Nunito:wght@600;700;800;900&display=swap">
<style>
  :root {
    --sleeve-bg: #e8eeb9;
    --leaf: #a4bd3c;
    --leaf-dark: #7e982b;
    --name-green: #6d8a2a;
    --berry-red: #a8332b;
    --outline: #3d3d33;
    --paper: #ffffff;
    --ink: #222222;
    --lid-rim: #8ba12f;
    --lid-tan: #ecd6a6;
    --lid-top-text: #c4d84e;
    --flavour-original: #a4bd3c;
    --flavour-raspberry: #c6756a;
    --flavour-cacao: #844d33;
  }
  html, body {
    margin: 0;
    width: 1200px;
    height: 1200px;
    overflow: hidden;
    background: var(--paper);
  }
  .artboard { display: block; width: 1200px; height: 1200px; }

  .sleeve-body { fill: var(--sleeve-bg); stroke: var(--outline); stroke-width: 1.2; }
  .flavour-band { fill: var(--flavour); }
  .sleeve--original { --flavour: var(--flavour-original); }
  .sleeve--raspberry { --flavour: var(--flavour-raspberry); }
  .sleeve--cacao { --flavour: var(--flavour-cacao); }
  .panel-divider { stroke: var(--outline); stroke-width: 1.2; }

  .info-box { fill: var(--leaf); }
  .info-box--dark { fill: var(--leaf-dark); }
  .info-text {
    font-family: "Nunito", sans-serif;
    font-weight: 800;
    font-size: 14px;
    fill: var(--sleeve-bg);
  }
  .info-text--centre { text-anchor: middle; }
  .address-text {
    font-family: "Nunito", sans-serif;
    font-weight: 700;
    font-size: 18px;
    fill: var(--sleeve-bg);
  }

  .nutrition-card { fill: var(--paper); stroke: var(--leaf); stroke-width: 3; }
  .nutrition-text {
    font-family: "Nunito", sans-serif;
    font-weight: 600;
    font-size: 10.5px;
    fill: var(--ink);
  }
  .nutrition-title { font-weight: 900; font-size: 14px; }
  .nutrition-rule { stroke: var(--ink); stroke-width: 0.8; }
  .num { text-anchor: end; }

  .front-panel { fill: var(--paper); }
  .brand-name {
    font-family: "Nunito", sans-serif;
    font-weight: 700;
    fill: var(--name-green);
    text-anchor: middle;
  }
  .claim-text {
    font-family: "Nunito", sans-serif;
    font-weight: 900;
    letter-spacing: 0.5px;
    text-anchor: middle;
  }
  .claim-text--free { fill: var(--leaf); }
  .claim-text--product { fill: var(--berry-red); }

  .flavour-name {
    font-family: "Nunito", sans-serif;
    font-weight: 900;
    fill: var(--paper);
  }

  .lid-rim { fill: var(--lid-rim); }
  .lid-face { fill: url(#lid-glow); }
  .lid-band { fill: var(--paper); }
  .lid .claim-text--free { fill: var(--lid-top-text); }
  .lid .claim-text--product { fill: var(--lid-tan); }
</style>
</head>
<body>
<svg class="artboard" viewBox="0 0 1440 1440" width="1200" height="1200" xmlns="http://www.w3.org/2000/svg">
  <defs>
    <linearGradient id="avocado-print-tone" x1="0" y1="0" x2="1" y2="1">
      <stop offset="0" stop-color="#dfe8a8"/>
      <stop offset="0.5" stop-color="#c9d98a"/>
      <stop offset="1" stop-color="#b4c96a"/>
    </linearGradient>
    <radialGradient id="lid-glow" cx="0.5" cy="0.5" r="0.5">
      <stop offset="0" stop-color="#7d4a2e"/>
      <stop offset="0.7" stop-color="#94663a"/>
      <stop offset="1" stop-color="#ad8f48"/>
    </radialGradient>

    <!-- tub sleeve, shared by every flavour -->
    <g id="sleeve">
      <path class="sleeve-body" d="M -605.2 73.1 A 2546 2546 0 0 1 605.2 73.1 L 490.1 543.2 A 2062 2062 0 0 0 -490.1 543.2 Z"/>
      <path class="flavour-band" d="M -261.7 13.5 A 2546 2546 0 0 1 0 0 L 0 484 A 2062 2062 0 0 0 -212 494.9 Z"/>
      <path fill="url(#avocado-print-tone)" role="img" aria-label="Avocado halves and leaves print" d="M 0 0 A 2546 2546 0 0 1 261.7 13.5 L 212 494.9 A 2062 2062 0 0 0 0 484 Z"/>
      <line class="panel-divider" x1="-261.7" y1="13.5" x2="-212" y2="494.9"/>
      <line class="panel-divider" x1="261.7" y1="13.5" x2="212" y2="494.9"/>

      <!-- back-left panel: nutrition and address -->
      <g class="panel panel--nutrition" transform="rotate(-9.8 0 2546)">
        <rect class="nutrition-card" x="-142" y="40" width="276" height="222" rx="12"/>
        <g class="nutrition-text">
          <text class="nutrition-title" x="-130" y="62">Nutrition</text>
          <text x="-130" y="76">Typical values</text>
          <text class="num" x="22" y="64">100ml</text>
          <text class="num" x="22" y="76">contains</text>
          <text x="34" y="64">%</text>
          <text x="34" y="76">RI*</text>
          <text class="num" x="126" y="60">RI* for an</text>
          <text class="num" x="126" y="72">average adult</text>
          <line class="nutrition-rule" x1="-132" y1="82" x2="126" y2="82"/>
          <text class="num" x="126" y="94">8400kJ</text>
          <text class="num" x="126" y="106">2000kcal</text>
          <text x="-130" y="104">Energy</text>
          <text x="2" y="94">kJ</text>
          <text x="-6" y="106">kcal</text>
          <text x="36" y="106">%</text>
          <text x="-130" y="124">Fat</text>
          <text x="8" y="124">g</text><text x="36" y="124">%</text>
          <text class="num" x="126" y="124">70g</text>
          <text x="-130" y="136">of which saturates</text>
          <text x="8" y="136">g</text><text x="36" y="136">%</text>
          <text class="num" x="126" y="136">20g</text>
          <text x="-130" y="148">Carbohydrate</text>
          <text x="8" y="148">g</text><text x="36" y="148">%</text>
          <text class="num" x="126" y="148">90g</text>
          <text x="-130" y="160">of which sugars</text>
          <text x="8" y="160">g</text>
          <text x="-130" y="172">Fibre</text>
          <text x="8" y="172">g</text>
          <text x="-130" y="184">Protein</text>
          <text x="8" y="184">g</text><text x="36" y="184">%</text>
          <text x="-130" y="196">Salt</text>
          <text x="8" y="196">g</text>
          <text class="num" x="126" y="196">6g</text>
          <line class="nutrition-rule" x1="-132" y1="202" x2="126" y2="202"/>
          <text x="-130" y="216">This pack contains</text>
          <text x="30" y="216">servings</text>
          <text x="-130" y="232">*Reference intake of an average</text>
          <text x="-130" y="245">adult (8400kJ / 2000kcal)</text>
        </g>
        <rect class="info-box" x="-150" y="285" width="296" height="118" rx="48"/>
        <text class="address-text" x="-40" y="336">Glenmorrow LTD,</text>
        <text class="address-text" x="-40" y="362">Wrenfold, WX4 2LP</text>
      </g>

      <!-- front panel: name and claims -->
      <g class="panel panel--front">
        <rect class="front-panel" x="-140" y="150" width="280" height="240" rx="24"/>
        <text class="claim-text claim-text--free" x="0" y="190" font-size="16">GLUTEN, SOYA, DAIRY, EGG</text>
        <text class="claim-text claim-text--free" x="0" y="212" font-size="16">AND NUT FREE</text>
        <text class="brand-name" x="0" y="278" font-size="40" textLength="250" lengthAdjust="spacingAndGlyphs">GLENMORROW</text>
        <text class="claim-text claim-text--product" x="0" y="334" font-size="16">COCONUT AND</text>
        <text class="claim-text claim-text--product" x="0" y="356" font-size="16">AVOCADO ICE CREAM</text>
      </g>

      <!-- back-right panel: ingredients, story, storage -->
      <g class="panel panel--info" transform="rotate(9.8 0 2546)">
        <rect class="info-box" x="-158" y="36" width="318" height="112" rx="30"/>
        <text class="info-text" x="-140" y="72">Ingredients: Coconut milk, Avocados,</text>
        <text class="info-text" x="-140" y="92">Agave Syrup, Lime Juice., Arrowroot, Guar</text>
        <text class="info-text" x="-140" y="112">Gum, Xanthan Gum, Salt</text>

        <rect class="info-box info-box--dark" x="-152" y="168" width="306" height="116" rx="56"/>
        <text class="info-text info-text--centre" x="0" y="200">Made from coconut flesh and creamy</text>
        <text class="info-text info-text--centre" x="0" y="219">avocado, our ice cream alternative offers</text>
        <text class="info-text info-text--centre" x="0" y="238">an indulgent dairy</text>
        <text class="info-text info-text--centre" x="0" y="257">free treat!</text>

        <rect class="info-box" x="-150" y="304" width="296" height="112" rx="30"/>
        <text class="info-text" x="-132" y="336">For best before see base.</text>
        <text class="info-text" x="-132" y="356">Storage conditions - keep frozen below</text>
        <text class="info-text" x="-132" y="376">-18° C best removed from freezer 5</text>
        <text class="info-text" x="-132" y="396">minutes before serving</text>
      </g>
    </g>
  </defs>

  <!-- 500ml sleeve: Original -->
  <g class="sleeve sleeve--original" transform="translate(640 122)">
    <use href="#sleeve"/>
    <text class="flavour-name" x="-148" y="478" font-size="27">ORIGINAL</text>
  </g>

  <!-- 100ml sleeve: Raspberry and Basil -->
  <g class="sleeve sleeve--raspberry" transform="translate(645 640) scale(0.6)">
    <use href="#sleeve"/>
    <text class="flavour-name" x="-160" y="446" font-size="22">RASPBERRY</text>
    <text class="flavour-name" x="-160" y="468" font-size="22">AND BASIL</text>
  </g>

  <!-- 100ml sleeve: Raw Cacao -->
  <g class="sleeve sleeve--cacao" transform="translate(642 975) scale(0.6)">
    <use href="#sleeve"/>
    <text class="flavour-name" x="-160" y="470" font-size="22">RAW CACAO</text>
  </g>

  <!-- lid -->
  <g class="lid" transform="translate(1230 1097)">
    <circle class="lid-rim" r="185"/>
    <circle class="lid-face" r="160"/>
    <text class="claim-text claim-text--free" x="0" y="-92" font-size="18">GLUTEN, SOYA, DAIRY, EGG</text>
    <text class="claim-text claim-text--free" x="0" y="-68" font-size="18">AND NUT FREE</text>
    <rect class="lid-band" x="-150" y="-44" width="300" height="80" rx="14"/>
    <text class="brand-name" x="0" y="13" font-size="44" textLength="270" lengthAdjust="spacingAndGlyphs">GLENMORROW</text>
    <text class="claim-text claim-text--product" x="0" y="72" font-size="18">COCONUT AND</text>
    <text class="claim-text claim-text--product" x="0" y="96" font-size="18">AVOCADO ICE CREAM</text>
  </g>
</svg>
</body>
</html>
```